Article/Flyer - Reservation of Rights

We would like an article that we normally produce through illustrator in a pdf format to be placed in a Word format. We have provided a sample article/flyer of our normal distribution style. We would like the outcome to be in WORD format

```html
<!DOCTYPE html>
<html lang="en">
<head>
<meta charset="utf-8">
<title>Reservation of Rights Letter – Ward &amp; Associates</title>
<link href="https://fonts.googleapis.com/css2?family=Tinos:wght@400;700&family=Roboto+Condensed:ital,wght@0,400;1,700&display=swap" rel="stylesheet">
<style>
  :root {
    --brand-red: #b3121b;
    --ink: #1d1d1f;
    --brand-ink: #3a3c40;
    --white: #ffffff;
    --panel: rgba(226, 226, 228, 0.93);
    --dark-1: #2b2c2e;
    --dark-2: #5b5d61;
    --sky-1: #f3f5f7;
    --sky-2: #cfd7de;
  }
  * { box-sizing: border-box; margin: 0; padding: 0; }
  html, body { width: 927px; height: 1200px; overflow: hidden; }
  body { position: relative; background: var(--dark-1); font-family: "Roboto Condensed", "Arial Narrow", sans-serif; color: var(--ink); }

  .backdrop {
    position: absolute; inset: 0;
    background: linear-gradient(160deg, var(--dark-2) 0%, var(--dark-1) 45%, #4a4b4e 75%, #2f3032 100%);
  }
  .masthead-photo {
    position: absolute; left: 0; top: 0; width: 927px; height: 282px;
    background: linear-gradient(180deg, var(--sky-1) 0%, #e6ebef 55%, var(--sky-2) 100%);
  }
  .team-photo {
    position: absolute; left: 560px; top: 0; width: 367px; height: 206px;
    background: linear-gradient(135deg, #c9d3db 0%, #9fa9b2 50%, #dfe3e6 100%);
  }

  .brand { position: absolute; left: 82px; top: 34px; font-family: "Tinos", "Times New Roman", serif; color: var(--brand-ink); }
  .brand-name { font-size: 40px; font-weight: 400; line-height: 1; }
  .brand-tagline { font-size: 16px; margin-top: 10px; }
  .brand-legal { font-size: 12px; margin: 10px 0 0 60px; }

  .intro {
    position: absolute; left: 70px; top: 208px; width: 770px;
    font-weight: 700; font-style: italic; font-size: 17px; line-height: 20px; color: var(--ink);
  }

  .section { position: absolute; left: 57px; width: 813px; }
  .section-title {
    background: var(--brand-red); color: var(--white);
    font-family: "Tinos", "Times New Roman", serif; font-weight: 700;
    font-size: 19.5px; text-align: center; height: 27px; line-height: 27px;
  }
  .section-body { padding: 4px 12px 6px 15px; }
  .section-body.solid { background: var(--white); font-size: 17px; line-height: 22px; }
  .section-body.solid p + p { margin-top: 6px; }
  .section-body.soft { background: var(--panel); font-size: 15.5px; line-height: 20.2px; }
  .section-body.soft p + p { margin-top: 5px; }

  .s1 { top: 288px; }
  .s2 { top: 582px; }
  .s3 { top: 969px; }
</style>
</head>
<body>
  <div class="backdrop" role="img" aria-label="Dark architectural photograph with glass building facade"></div>
  <div class="masthead-photo" role="img" aria-label="Bright sky and glass office tower"></div>
  <div class="team-photo" role="img" aria-label="Photograph of design professionals reviewing plans at a desk"></div>

  <header class="brand">
    <div class="brand-name">Ward &amp; Associates</div>
    <div class="brand-tagline">Serving Architects, Engineers and Environmental Consultants</div>
    <div class="brand-legal">Northline Partners of Oregon, LLC dba Ward &amp; Associates</div>
  </header>

  <p class="intro">Reporting a claim or potential claim to your professional liability insurance company will trigger a fair amount of return correspondence that often creates confusion rather than clarity.<br>One document that commonly falls into this category is the Reservation of Rights Letter.</p>

  <section class="section s1">
    <h2 class="section-title">WHAT IS THE RESERVATION OF RIGHTS LETTER</h2>
    <div class="section-body solid">
      <p>The Reservation of Rights Letter is a normal part of the insurance claims process. Its purpose is to provide notification from the insurance company to the policy holder that coverage may not apply. While this often comes as alarming news, the Reservation of Rights Letter should not be mistaken as an outright denial -- it does not automatically mean that coverage is being or will be denied.</p>
      <p>This standard correspondence is routinely sent to comply with state laws and preserve the insurance company’s legal ability to deny some, or all, of the claim pending further investigation while the claim is ongoing and being handled by the insurance company. Failure to send the letter could be considered a waiver of their rights at a later time.</p>
      <p>Because information is vague in the early stages of a claim and often is limited to unsubstantiated allegations and a few facts, the Reservation of Rights Letter protects the insurance company’s interests to later deny coverage in whole or part based on evidence revealed during claims handling.</p>
    </div>
  </section>

  <section class="section s2">
    <h2 class="section-title">INTERPRETING THE LETTER</h2>
    <div class="section-body soft">
      <p>Most of the time the Reservation of Rights Letter is a generic form letter that states your insurance company is proceeding with handling your claim but reserves the right to deny coverage later on based upon any information that reveals reason to deny.</p>
      <p>Legitimate reasons an insurance company may deny coverage include when the loss occurred in relation to your retroactive date, specific exclusions in the policy language, prior knowledge of the incident, and coverage by another policy, among others.</p>
      <p>If the insurance company believes there may be reason for denial at the time the Reservation of Rights Letter is sent, it will be stated in the letter. For example, if the claim alleges breach of warranty, the letter will state that warranties are specifically excluded by the policy and it will include the policy language to demonstrate the exclusion.</p>
      <p>Even when specific reasons for potential coverage denial are cited, it is important to note that this is not a final verdict nor does it mean complete lack of coverage. Generally the insurance company is obligated to help you if any of your claims are covered by your insurance policy – there is a duty to defend. In cases such as the scenario above, circumstances of the claim will influence what is covered and what may be subject to exclusion.<br>Based on investigative conclusions, the insurance company may not be obligated to pay the damages for certain types or aspects of claims.</p>
    </div>
  </section>

  <section class="section s3">
    <h2 class="section-title">HOW TO PROCEED</h2>
    <div class="section-body soft">
      <p>Although the intent of the Reservation of Rights Letter is to protect the insurance company’s interests, it also alerts the policy holder to the fact that some elements of a claim may not be covered and therefore allows the insured to take steps to protect its potentially uninsured interests.</p>
      <p>However, receiving the Reservation of Rights Letter and even the insurance company’s interpretation of the policy language or law that they believe points toward coverage declination does not mean that you are automatically required to accept a denial of coverage.</p>
      <p>The best thing to do upon receiving the letter is to contact your broker and work closely with them and the insurance company claims handling department to ensure the prompt and fair handling of your claim.</p>
    </div>
  </section>
</body>
</html>
```